Seller Looking for a luxurious diverse ethnic look...stunning but not overly seductive

I need a web Design for a company based in NEW YORK CITY called Velvet Harbor LLC. Initially I will be selling clothing and accessories as well as electronics on Tradora and hope to branch out. I want the whole experience for my customers and people I will buy from when they deal with me to be confident that this will be a velvet harbor and luxurious transaction.
Updates

Project Deadline Extended Reason: As I keep getting these great designs I continue to get more ideas and feel more time will help get us there. Added Thursday, July 16, 2015

Target Market(s)

ages 20-60

Industry/Entity Type

Clothing

Number of Pages Required

1 page

Font styles to use
Script

Colors
b768aa

Requirements
Must have
• Sleek and Luxurious feel and modern. I would like the page to look startling stunning yet not overly seductive and to include ethnic diversity. I like the illusion not knowing what the sight is selling since I am not targeting one area.
Should not have
• Do not want it to look generic or traditional

```html
<!DOCTYPE html>
<html lang="en">
<head>
<meta charset="utf-8">
<title>Velvet Harbor</title>
<link href="https://fonts.googleapis.com/css2?family=Chewy&family=Open+Sans:wght@400;600;700&display=swap" rel="stylesheet">
<style>
:root{
  --plum:#b768aa;
  --plum-dark:#94508a;
  --plum-soft:#f3ddef;
  --plum-mid:#c98abf;
  --ink:#333333;
  --muted:#8a8a8a;
  --line:#e3e3e3;
  --page:#f4f4f4;
  --foot:#2a2a2a;
  --foot-text:#b9b9b9;
  --white:#ffffff;
}
*{box-sizing:border-box;margin:0;padding:0}
html,body{width:747px;height:1200px;overflow:hidden}
body{position:relative;background:var(--page);font-family:"Open Sans",Arial,sans-serif;color:var(--ink);font-size:8px}
ul{list-style:none}

.utility-bar{position:absolute;top:0;left:0;width:747px;height:25px;background:var(--white);display:flex;align-items:center;justify-content:space-between;padding:0 62px;color:var(--muted);font-size:7px}
.utility-bar .links span{margin-right:10px}

.site-header{position:absolute;top:25px;left:0;width:747px;height:70px;background:var(--plum)}
.brand{position:absolute;left:62px;top:24px;display:flex;align-items:center;gap:7px}
.brand-dot{width:14px;height:14px;border-radius:50%;background:var(--white)}
.brand-name{color:var(--white);font-family:"Open Sans",Arial,sans-serif;font-weight:700;font-size:15px;text-transform:uppercase;letter-spacing:1px;white-space:nowrap}
.contact-line{position:absolute;right:62px;top:18px;color:var(--white);font-size:9px;font-weight:600;display:flex;align-items:center;gap:5px}
.main-nav{position:absolute;right:62px;top:50px;display:flex;gap:16px;color:var(--white);font-size:7.5px;font-weight:700;text-transform:uppercase}

.hero{position:absolute;top:95px;left:0;width:747px;height:378px;background:linear-gradient(100deg,#c7a9a2 0%,#e6d7d2 35%,#c45f96 62%,#d9c9c6 100%)}
.hero-title{position:absolute;left:55px;top:140px;font-family:"Chewy",cursive;line-height:1}
.hero-title .lead{display:block;color:var(--white);font-size:40px;letter-spacing:1px}
.hero-title .name{display:block;color:var(--plum);font-size:44px;letter-spacing:2px;text-transform:uppercase}
.hero-arrow{position:absolute;top:168px;width:22px;height:40px;background:rgba(0,0,0,.35);display:flex;align-items:center;justify-content:center}
.hero-arrow.prev{left:0}.hero-arrow.next{right:0}

.content{position:absolute;top:485px;left:62px;width:623px;height:500px;background:var(--white)}
.sidebar{position:absolute;left:0;top:13px;width:145px}
.side-block{background:var(--plum-soft)}
.side-block h3{background:var(--plum);color:var(--white);font-size:8px;font-weight:700;text-transform:uppercase;padding:8px 10px}
.side-block li{padding:4.5px 10px;font-size:6.5px;color:#6d4a66;text-transform:uppercase;border-bottom:1px solid #ead0e5}
.side-block.care{background:var(--plum-mid);margin-top:12px}
.side-block.care li{color:var(--white);border-bottom-color:#d4a0cb}

.new-arrivals{position:absolute;left:165px;top:15px;width:450px}
.section-tab{display:inline-block;background:var(--plum);color:var(--white);font-weight:700;font-size:9px;padding:6px 12px;text-transform:uppercase}
.section-rule{height:2px;background:var(--plum);margin-bottom:12px}
.product-grid{display:grid;grid-template-columns:repeat(3,140px);gap:14px 14px}
.product-card{height:192px;border:1px solid var(--line);padding:8px;text-align:center}
.product-photo{height:112px;margin-bottom:8px}
.product-card h4{color:var(--plum);font-size:6.5px;font-weight:700;text-transform:uppercase}
.product-card p{color:var(--muted);font-size:6px;margin:3px 0 6px}
.product-card .view{display:block;background:var(--page);border:1px solid var(--line);padding:4px;font-size:6px;color:var(--muted)}
.product-card.featured .view{background:var(--plum);color:var(--white);border-color:var(--plum)}

.pagination{position:absolute;left:165px;top:475px;width:450px;display:flex;justify-content:space-between;align-items:center;font-size:7px;color:var(--muted);border-top:1px solid var(--line);padding-top:6px}
.pages{display:flex;gap:6px}
.pages span{padding:2px 5px;border:1px solid var(--line)}
.pages .current{background:var(--plum);color:var(--white);border-color:var(--plum)}

.site-footer{position:absolute;top:996px;left:0;width:747px;height:204px;background:var(--foot);color:var(--foot-text)}
.foot-col{position:absolute;top:20px;width:150px}
.foot-col h5{color:var(--white);font-size:8px;text-transform:uppercase;margin-bottom:8px;padding-bottom:5px;border-bottom:1px solid #444}
.foot-col li{font-size:6.5px;padding:3px 0}
.foot-col li::before{content:"› ";color:var(--plum)}
.foot-bottom{position:absolute;left:62px;right:62px;top:160px;border-top:1px solid #444;padding-top:10px;display:flex;justify-content:space-between;align-items:center;font-size:6.5px}
.payments{display:flex;gap:8px;align-items:center}
.payments span{background:#3d3d3d;color:var(--white);font-size:7px;font-weight:700;padding:3px 6px}
.payments .market{background:none;font-size:12px}
</style>
</head>
<body>

<div class="utility-bar">
  <div class="links"><span>Welcome guest</span><span>Register</span><span>Account</span><span>Wishlist</span></div>
  <div>Sign in</div>
</div>

<header class="site-header">
  <div class="brand"><span class="brand-dot"></span><span class="brand-name">velvet harbor</span></div>
  <div class="contact-line">
    <svg width="10" height="10" viewBox="0 0 24 24"><path fill="#fff" d="M6.6 10.8a15 15 0 0 0 6.6 6.6l2.2-2.2c.3-.3.7-.4 1-.2 1.1.4 2.3.6 3.6.6.6 0 1 .4 1 1V20c0 .6-.4 1-1 1A17 17 0 0 1 3 4c0-.6.4-1 1-1h3.5c.6 0 1 .4 1 1 0 1.3.2 2.5.6 3.6.1.3 0 .7-.2 1z"/></svg>
    CALL US : 555 010 2468
  </div>
  <nav class="main-nav"><span>Home</span><span>About us</span><span>Designs</span><span>Shoes</span><span>Bags</span><span>Customer care</span><span>Contact us</span></nav>
</header>

<section class="hero" role="img" aria-label="Smiling couple holding colourful shopping bags in a mall">
  <h1 class="hero-title"><span class="lead">WELCOME TO</span><span class="name">Velvet Harbor</span></h1>
  <div class="hero-arrow prev"><svg width="8" height="12" viewBox="0 0 8 12"><path d="M7 1 2 6l5 5" stroke="#fff" stroke-width="2" fill="none"/></svg></div>
  <div class="hero-arrow next"><svg width="8" height="12" viewBox="0 0 8 12"><path d="m1 1 5 5-5 5" stroke="#fff" stroke-width="2" fill="none"/></svg></div>
</section>

<main class="content">
  <aside class="sidebar">
    <div class="side-block">
      <h3>Shop categories</h3>
      <ul><li>Party wear</li><li>Accessories</li><li>Bottoms</li><li>Dresses</li><li>Gift sets</li><li>Footwear</li><li>Bags</li><li>Shoes</li><li>Sale</li></ul>
    </div>
    <div class="side-block care">
      <h3>Customer care</h3>
      <ul><li>Contact us</li><li>Gift card</li><li>Shipping</li><li>Returns</li><li>Payments</li><li>FAQ</li><li>Privacy policy</li><li>Order tracking</li></ul>
    </div>
  </aside>

  <section class="new-arrivals">
    <div class="section-tab">What's new</div>
    <div class="section-rule"></div>
    <div class="product-grid">
      <article class="product-card featured"><div class="product-photo" role="img" aria-label="Woman in red dress holding shopping bags" style="background:linear-gradient(#fff,#f3d6d6)"></div><h4>New Listed Item</h4><p>Shop the collection</p><span class="view">View Listing</span></article>
      <article class="product-card"><div class="product-photo" role="img" aria-label="Blue leather handbag" style="background:linear-gradient(#fff,#dcdcf5)"></div><h4>New Listed Item</h4><p>Shop the collection</p><span class="view">View Listing</span></article>
      <article class="product-card"><div class="product-photo" role="img" aria-label="Group of women with shopping bags" style="background:linear-gradient(#fff,#f5e3c8)"></div><h4>New Listed Item</h4><p>Shop the collection</p><span class="view">View Listing</span></article>
      <article class="product-card"><div class="product-photo" role="img" aria-label="Navy canvas sneakers" style="background:linear-gradient(#fff,#dde2ea)"></div><h4>New Listed Item</h4><p>Shop the collection</p><span class="view">View Listing</span></article>
      <article class="product-card"><div class="product-photo" role="img" aria-label="Black handbag" style="background:linear-gradient(#fff,#e2dede)"></div><h4>New Listed Item</h4><p>Shop the collection</p><span class="view">View Listing</span></article>
      <article class="product-card"><div class="product-photo" role="img" aria-label="Tablet computer" style="background:linear-gradient(#fff,#d8e6f2)"></div><h4>New Listed Item</h4><p>Shop the collection</p><span class="view">View Listing</span></article>
    </div>
  </section>

  <nav class="pagination">
    <span>‹ Previous</span>
    <div class="pages"><span>1</span><span>13</span><span>14</span><span class="current">15</span><span>16</span><span>17</span><span>18</span></div>
    <span>Next ›</span>
  </nav>
</main>

<footer class="site-footer">
  <div class="foot-col" style="left:62px"><h5>My account</h5><ul><li>My orders</li><li>My credit slips</li><li>My addresses</li><li>My personal info</li></ul></div>
  <div class="foot-col" style="left:207px"><h5>Information</h5><ul><li>Specials</li><li>New products</li><li>Top sellers</li><li>Contact us</li><li>About us</li></ul></div>
  <div class="foot-col" style="left:371px"><h5>Customer service</h5><ul><li>Add to cart</li><li>Help desk</li><li>Payment methods</li><li>Custom work</li><li>Promotions</li></ul></div>
  <div class="foot-col" style="left:538px"><h5>Contact us</h5><ul><li>New York storefront</li><li>Live support</li><li>Shop on Tradora</li><li>Open weekdays</li><li>Send inquiry</li></ul></div>
  <div class="foot-bottom">
    <span>© 2015 Velvet Harbor LLC. All rights reserved.</span>
    <div class="payments"><span>Brimcard</span><span>Ruvio</span><span>Silvane Pay</span><span class="market">Tradora</span></div>
  </div>
</footer>

</body>
</html>
```